Plot Lantern Website Design

At Plot Lantern we’re about to launch an exciting new product in the Project Management space. We aim to simplify the process of reporting on-site work activities. Our flagship product, Briskline, provides users the ability to record work activities as they are performed with automatic reporting back to home base using a smartphone.
The website will be the primary face of the company, and is to be used for advertising the product, for sales, and for subscribers to manage their data. We need a site with a clean, simple appearance that is easy to navigate. To give you a better idea of what we need, our brief includes a wire frame template for the site.
We’d like you to produce a single page site design as shown in the wireframe. We’re looking for a Web 2.0 design and can implement any animation effects that your design needs, just provide us with some notes on how each element should behave. You’re free to design whatever you like within the bounds set out below. After the design is complete the team at Plot Lantern will turn it into a functional website.
-Logo provided. We’d like the website to adhere to work with the logo either using the same colour theme (blue, black, grey) or one you think is complementary.
-Site design to include logo and ‘PlotLantern’ as title at the top of the page.
-Use suitable stock images when you need to place an image.
-Ensure you provide links for the images you use so we can purchase them if we choose.
-Link to hero image example http://www.framevaultpics.example/photo/worker-holding-handset-at-factory-yard-58193047. We aren’t completely happy with this image so we’re open for suggestions of superior images.
-Styling for all visual aspects of the site, including colors, font selection, sizing, placement, shadowing, backgrounds, images, layout, etc.
-Styling of text boxes, ie user login, sign up etc.
-‘Site map’ links at the bottom of page
-Styled form for user sign up, modal acceptable.
link to the Orbix App Bazaar.
-Site may need to be responsive to screen size, mobile, tablet, desktop. Aim for desktop but consider other formats. Styling to accomodate. Please use a standardised grid system.
Target Market(s)
Construction professionals, ie Contract Administrators, Project Managers and trades people
Industry/Entity Type
Advertising
Requirements
Must have
- See brief above
Nice to have
- See brief above
Should not have
- See brief above

```html
<!DOCTYPE html>
<html lang="en">
<head>
<meta charset="utf-8">
<title>PlotLantern</title>
<link rel="stylesheet" href="https://fonts.googleapis.com/css2?family=Exo+2:ital,wght@0,400;0,500;0,600;0,700;1,600&display=swap">
<style>
:root{
  --blue:#0a66b7;
  --blue-dark:#08559a;
  --ink:#1d1d1d;
  --text:#555;
  --muted:#8a8a8a;
  --panel:#f4f4f4;
  --band:#ececec;
  --line:#cfcfcf;
  --dark:#2b2b2b;
  --white:#fff;
}
*{box-sizing:border-box;margin:0;padding:0}
html,body{width:1200px;height:2514px;overflow:hidden}
body{position:relative;background:var(--white);font-family:"Exo 2",Arial,sans-serif;color:var(--ink)}
.abs{position:absolute}

/* header */
.brand{left:161px;top:40px;display:flex;align-items:center;gap:10px;font-size:27px;font-weight:700;color:var(--ink);letter-spacing:-.5px}
.brand-mark{width:26px;height:26px;background:var(--blue)}
.search{left:396px;top:45px;width:276px;height:22px;background:#ececec;font-size:9px;color:#777;padding:5px 14px}
.nav{top:47px;font-size:15px;color:var(--ink)}
.nav.active{color:var(--blue)}
.nav::after{content:"";display:inline-block;width:5px;height:5px;border-right:1.5px solid currentColor;border-bottom:1.5px solid currentColor;transform:rotate(45deg);margin:0 0 3px 7px}
.btn-sm{top:44px;height:25px;font-size:9px;font-weight:600;display:flex;align-items:center;justify-content:center;border:1.5px solid var(--blue)}
.btn-login{left:925px;width:52px;background:var(--blue);color:var(--white)}
.btn-signup{left:985px;width:52px;color:var(--blue)}

/* hero */
.hero{left:161px;top:112px;width:878px;height:376px;background:linear-gradient(180deg,#cfe0ee 0%,#b9c6c9 55%,#d8cdb8 100%)}
.hero-dots{left:565px;top:465px;display:flex;gap:6px}
.hero-dots span{width:16px;height:16px;border-radius:50%;background:var(--blue)}
.hero-dots span.on{background:var(--dark)}
.hero-band{left:161px;top:488px;width:878px;height:52px;background:var(--blue);color:var(--white);font-size:27px;font-weight:600;display:flex;align-items:center;justify-content:center}
.arrow-round{width:26px;height:26px;border-radius:50%;display:flex;align-items:center;justify-content:center}

/* newsletter */
.newsletter{left:161px;top:585px;width:427px;height:300px;background:var(--panel)}
.newsletter h2{position:absolute;left:35px;top:37px;font-size:21px;font-weight:500}
.newsletter p{position:absolute;left:35px;top:74px;width:360px;font-size:11px;line-height:18px;color:var(--text)}
.email-field{left:37px;top:146px;width:350px;height:45px;background:var(--white);border:1px solid var(--line);font-size:10px;color:#888;padding:14px 0 0 57px}
.btn-subscribe{left:37px;top:198px;width:350px;height:45px;background:var(--blue);color:var(--white);font-size:15px;font-weight:600;display:flex;align-items:center;justify-content:center}

.what h2{font-size:20px;font-weight:500}
.what p{font-size:10px;color:var(--text);line-height:13px;width:420px;margin-top:4px}
.video{left:613px;top:649px;width:423px;height:236px;background:linear-gradient(180deg,#8a97a8,#4b5563)}
.video-label{left:0;top:82px;width:423px;text-align:center;color:var(--white);font-size:17px}
.video-bar{left:0;top:204px;width:423px;height:32px;background:rgba(0,0,0,.55)}

/* cta band */
.cta-band{left:0;top:930px;width:1200px;height:299px;background:var(--panel)}
.cta-title{left:0;top:1000px;width:1200px;text-align:center;font-size:19px;font-weight:600}
.cta-text{left:290px;top:1045px;width:620px;text-align:center;font-size:10px;line-height:14px;color:var(--text)}
.cta-btn{top:1108px;height:45px;background:var(--blue);color:var(--white);font-size:12px;font-weight:600;display:flex;align-items:center;justify-content:center;gap:10px}
.cta-btn.store{background:var(--dark);font-size:11px;line-height:11px}

/* features */
.features h2{font-size:20px;font-weight:500}
.features p{font-size:8px;color:var(--muted);margin-top:4px;width:430px}
.tile{width:202px;height:149px}
.tile-caption{left:0;top:40px;width:202px;text-align:center;color:var(--white);font-size:11px;line-height:13px}
.tile-caption b{display:block;font-size:17px;font-weight:600;margin-bottom:3px}

.query{left:613px;top:1282px;width:428px;height:444px;background:var(--panel)}
.label{left:652px;font-size:10px;color:var(--ink)}
.field{left:652px;width:352px;height:21px;background:var(--white);border:1px solid var(--line)}
.progress{left:652px;top:1322px;width:352px;height:22px;background:var(--white);border:1px solid var(--line)}
.progress-fill{left:0;top:0;width:246px;height:20px;background:repeating-linear-gradient(135deg,var(--blue) 0 6px,#2a7cc6 6px 12px)}
.btn-submit{left:652px;top:1683px;width:352px;height:22px;background:var(--blue);color:var(--white);font-size:10px;font-weight:600;display:flex;align-items:center;justify-content:center}

/* about */
.about{left:0;top:1756px;width:1200px;height:227px;background:var(--blue);color:var(--white)}
.about h2{position:absolute;left:161px;top:57px;font-size:23px;font-weight:600}
.about p{position:absolute;top:101px;width:427px;font-size:10.5px;line-height:15px;font-weight:500}

/* testimonials */
.reviews{left:0;top:1983px;width:1200px;height:263px;background:var(--band)}
.avatar{width:74px;height:74px;border-radius:50%;border:3px solid var(--blue);background:linear-gradient(180deg,#d9d9d9,#9fa7ad)}
.person{width:140px;text-align:center;font-size:10px;font-weight:600}
.person span{display:block;font-weight:400;color:var(--muted);font-size:9px;margin-top:4px}
.quote{top:2038px;width:280px;height:149px;background:var(--blue)}
.quote-bar{left:0;top:0;width:33px;height:149px;background:var(--dark);color:var(--white);font-size:30px;font-weight:700;text-align:center;line-height:46px}
.quote p{position:absolute;left:47px;top:26px;width:220px;color:var(--white);font-size:11.5px;line-height:17px;font-style:italic;font-weight:600}

/* footer */
.foot-head{top:2318px;font-size:11px;font-weight:600}
.foot-links{top:2343px;font-size:9.5px;line-height:25px;color:var(--text)}
.social{top:2321px;width:37px;height:37px}
.foot-title{left:761px;top:2370px;font-size:15px}
.foot-text{left:761px;top:2392px;width:280px;font-size:10px;line-height:14px;color:var(--text)}
.copyright{left:0;top:2484px;width:1200px;height:30px;background:#e4e4e4;font-size:10px;text-align:center;line-height:30px;color:var(--ink)}
</style>
</head>
<body>

<header>
  <div class="abs brand"><span class="brand-mark"></span>PLOTLANTERN</div>
  <div class="abs search">SEARCH HERE...</div>
  <div class="abs nav active" style="left:687px">Briskline</div>
  <div class="abs nav" style="left:778px">About</div>
  <div class="abs nav" style="left:841px">Support</div>
  <div class="abs btn-sm btn-login">LOGIN</div>
  <div class="abs btn-sm btn-signup">SIGN UP</div>
</header>

<section class="hero-slider">
  <div class="abs hero" role="img" aria-label="Engineer in a hard hat using a smartphone at an industrial site"></div>
  <div class="abs hero-dots"><span></span><span class="on"></span><span></span></div>
  <div class="abs hero-band">Wellcome to PLOTLANTERN</div>
  <div class="abs arrow-round" style="left:124px;top:285px;border:2px solid #bbb">
    <svg width="10" height="10" viewBox="0 0 10 10"><path d="M7 1 3 5l4 4" fill="none" stroke="#bbb" stroke-width="2"/></svg></div>
  <div class="abs arrow-round" style="left:1046px;top:285px;border:2px solid var(--blue)">
    <svg width="10" height="10" viewBox="0 0 10 10"><path d="M3 1l4 4-4 4" fill="none" stroke="#0a66b7" stroke-width="2"/></svg></div>
</section>

<section class="abs newsletter">
  <h2>Subcribe To our Newsletter</h2>
  <p>Lorem Ipsum is simply dummy text of the printing and typesetting industry. Lorem Ipsum has been the industry's standard dummy text ever since the 1500s.</p>
  <div class="abs email-field">Enter your email address here..
    <svg class="abs" style="left:16px;top:13px" width="18" height="16" viewBox="0 0 18 16"><path d="M1 8 17 1 12 15 9 9Z" fill="none" stroke="#999" stroke-width="1.5"/></svg>
  </div>
  <div class="abs btn-subscribe">SUBSCRIBE NOW</div>
</section>

<section class="abs what" style="left:613px;top:580px">
  <h2>WHAT WE DO</h2>
  <p>Democracy inspire breakthroughs, Mira Holt; inspiration raise awareness natural resources. Governance impact; transformative.</p>
</section>
<div class="abs video" role="img" aria-label="Video still of two site engineers in hard hats inspecting a plant">
  <div class="abs video-label">Play Video</div>
  <svg class="abs" style="left:199px;top:108px" width="26" height="20" viewBox="0 0 26 20"><rect width="26" height="20" rx="3" fill="#fff"/><path d="M10 5v10l8-5z" fill="#333"/></svg>
  <div class="abs video-bar">
    <svg class="abs" style="left:14px;top:9px" width="12" height="14" viewBox="0 0 12 14"><path d="M0 0v14l12-7z" fill="#fff"/></svg>
    <div class="abs" style="left:70px;top:14px;width:260px;height:4px;background:#666"></div>
    <div class="abs" style="left:70px;top:14px;width:70px;height:4px;background:var(--blue)"></div>
    <div class="abs" style="left:370px;top:9px;color:#3b8fe0;font-size:11px;font-weight:700;font-style:italic">HD</div>
  </div>
</div>

<section class="cta">
  <div class="abs cta-band"></div>
  <h2 class="abs cta-title">Lorem ipsum dolor sit amet, maiores.</h2>
  <p class="abs cta-text">Lorem ipsum dolor sit amet, maiores ornare ac fermentum, imperdiet ut vivamus a, nam lectus at nunc. Quam euismod sem, semper utin eget sapien sed, sit duis vestibulum ultricies, placerat morbi amet vel.</p>
  <div class="abs cta-btn store" style="left:161px;width:173px"><span>Get Briskline<br><small style="font-size:8px;font-weight:400">from the Orbix App Bazaar</small></span></div>
  <div class="abs cta-btn" style="left:337px;width:173px">See our pricing <b style="font-size:18px">$</b></div>
  <div class="abs cta-btn" style="left:514px;width:173px">Case Study
    <svg width="14" height="18" viewBox="0 0 14 18"><path d="M1 1h8l4 4v12H1z" fill="#fff"/><path d="M4 9h6M4 12h6" stroke="#0a66b7"/></svg></div>
  <div class="abs cta-btn" style="left:691px;width:173px">About Us
    <svg width="18" height="18" viewBox="0 0 18 18"><circle cx="9" cy="9" r="8" fill="#fff"/><path d="M9 8v6" stroke="#0a66b7" stroke-width="2"/><circle cx="9" cy="5" r="1.3" fill="#0a66b7"/></svg></div>
  <div class="abs cta-btn" style="left:867px;width:172px">Contact Us
    <svg width="18" height="18" viewBox="0 0 18 18"><rect width="18" height="18" rx="3" fill="#fff"/><path d="M5 4c-1 2 1 6 4 8s5 2 5 1l-2-2-2 1-3-3 1-2z" fill="#0a66b7"/></svg></div>
</section>

<section class="abs features" style="left:161px;top:1310px">
  <h2>OUR FEATURE PRODUCT</h2>
  <p>Lorem Ipsum is simply dummy text of the printing and typesetting industry. Lorem Ipsum has been the industry's standard dummy text ever since</p>
</section>
<div class="abs tile" style="left:161px;top:1376px;background:linear-gradient(180deg,#5d88b8,#2e5f93)" role="img" aria-label="Engineers in hard hats shaking hands on site">
  <div class="abs tile-caption"><b>Eros metus quam.</b>Lorem ipsum dolor sit amet, maiores ornare ac fermentum, imperdiet ut vivamus a, nam lect</div>
</div>
<div class="abs tile" style="left:387px;top:1376px;background:linear-gradient(180deg,#c9dbe9,#c8bfa8)" role="img" aria-label="Engineer with smartphone beside an excavator"></div>
<div class="abs tile" style="left:161px;top:1549px;background:linear-gradient(180deg,#8fb5de,#c7b999)" role="img" aria-label="Engineer holding a tablet at a construction site"></div>
<div class="abs tile" style="left:387px;top:1549px;background:linear-gradient(180deg,#6e6e6e,#2d2d2d)" role="img" aria-label="Worker in a blue hard hat holding a tablet"></div>

<section class="query-form">
  <div class="abs query"></div>
  <div class="abs label" style="top:1300px;font-size:15px">Payment Progress</div>
  <div class="abs progress"><div class="abs progress-fill"></div><span class="abs" style="left:308px;top:3px;font-size:13px;color:var(--blue)">75%</span></div>
  <div class="abs label" style="top:1350px">Enter Name :</div><div class="abs field" style="top:1368px"></div>
  <div class="abs label" style="top:1397px">Company Name :</div><div class="abs field" style="top:1415px"></div>
  <div class="abs label" style="top:1444px">Enter Email :</div><div class="abs field" style="top:1461px"></div>
  <div class="abs label" style="top:1491px">Enter Phone No :</div><div class="abs field" style="top:1508px;width:179px"></div>
  <div class="abs label" style="left:860px;top:1513px">Request Call Back</div>
  <div class="abs" style="left:982px;top:1510px;width:20px;height:20px;background:var(--white);border:1px solid var(--line)">
    <svg width="18" height="18" viewBox="0 0 18 18"><path d="M4 9l3 3 7-7" fill="none" stroke="#0a66b7" stroke-width="2.2"/></svg></div>
  <div class="abs label" style="top:1536px">How did you hear about us:</div>
  <div class="abs field" style="top:1554px;width:179px;font-size:9.5px;padding:4px 12px">searchly
    <svg class="abs" style="left:158px;top:8px" width="8" height="5" viewBox="0 0 8 5"><path d="M0 0h8L4 5z" fill="#333"/></svg></div>
  <div class="abs label" style="top:1583px">Enter your massage :</div>
  <div class="abs field" style="top:1601px;height:73px"></div>
  <div class="abs btn-submit">SUBMIT QUERY</div>
</section>

<section class="abs about">
  <h2>ABOUT US</h2>
  <p style="left:161px">Lorem Ipsum is simply dummy text of the printing and typesetting industry. Lorem Ipsum has been the industry's standard dummy text ever since the 1500s, when an unknown printer took a galley of type and scrambled it to make a type specimen book. It has survived not only five centuries</p>
  <p style="left:612px">Lorem Ipsum is simply dummy text of the printing and typesetting industry. Lorem Ipsum has been the industry's standard dummy text ever since the 1500s, when an unknown printer took a galley of type and scrambled it to make a type specimen book. It has survived not only five centuries</p>
</section>

<section class="testimonials">
  <div class="abs reviews"></div>
  <div class="abs arrow-round" style="left:118px;top:2099px;background:var(--blue)">
    <svg width="10" height="10" viewBox="0 0 10 10"><path d="M7 1 3 5l4 4" fill="none" stroke="#fff" stroke-width="2"/></svg></div>
  <div class="abs arrow-round" style="left:1054px;top:2099px;background:var(--white);border:1.5px solid var(--blue)">
    <svg width="10" height="10" viewBox="0 0 10 10"><path d="M3 1l4 4-4 4" fill="none" stroke="#0a66b7" stroke-width="2"/></svg></div>

  <div class="abs avatar" style="left:209px;top:2045px" role="img" aria-label="Portrait of Marlon Pryce"></div>
  <div class="abs person" style="left:176px;top:2134px">Marlon Pryce<span>Lead Software Designer</span></div>
  <div class="abs quote" style="left:307px"><div class="abs quote-bar">“</div>
    <p>Lorem ipsum dolor sit amet, consectetur adipiscing elit, sed do eiusmod tempor incididunt ut labore et dolore magna aliqua. Ut enim ad minim veniam, quis trud exercitation ullamco laboris nisi ut aliquip ex ea commodo</p></div>

  <div class="abs avatar" style="left:653px;top:2045px" role="img" aria-label="Portrait of Delia Frankes"></div>
  <div class="abs person" style="left:620px;top:2134px">Delia Frankes<span>Lead Software Engineer</span></div>
  <div class="abs quote" style="left:761px;width:278px"><div class="abs quote-bar">“</div>
    <p>Lorem ipsum dolor sit amet, consectetur adipiscing elit, sed do eiusmod tempor incididunt ut labore et dolore magna aliqua. Ut enim ad minim veniam, quis trud exercitation ullamco laboris nisi ut aliquip ex ea commodo</p></div>
</section>

<footer>
  <div class="abs foot-head" style="left:161px">ABOUT US</div>
  <div class="abs foot-links" style="left:178px">COMPANY<br>PRESS</div>
  <div class="abs foot-head" style="left:312px">QUICK START</div>
  <div class="abs foot-links" style="left:327px">PRODUCT<br>PRICING<br>CASE STUDY</div>
  <div class="abs foot-head" style="left:461px">SUPORT</div>
  <div class="abs foot-links" style="left:477px">CONTACT US<br>TERMS OF USE<br>PRIVACY<br>HELP</div>
  <div class="abs foot-head" style="left:612px">DOWNLOAD</div>
  <div class="abs foot-links" style="left:629px">ORBIXOS</div>

  <div class="abs social" style="left:761px;background:#3b5a9a"></div>
  <div class="abs social" style="left:810px;background:#3fa9e8"></div>
  <div class="abs social" style="left:859px;background:#d9363e"></div>
  <div class="abs social" style="left:908px;background:#3b5a9a"></div>
  <div class="abs foot-title">Wellcome to PLOTLANTERN</div>
  <p class="abs foot-text">Lorem Ipsum is simply dummy text of the printing and typesetting industry. Lorem Ipsum has been the industry's standard dummy text ever since</p>
  <div class="abs copyright">© 2014 plotlantern.example.</div>
</footer>

</body>
</html>
```